Alpenmark Banner

Hi boys and girls :)

We have a little project 4u.

We need a banner in 4 sizes :

Leaderboard: 728*90
Wide SkyScraper: 160*600
Medium Rectangle: 300*250
Ribbon (special format): 990*45

Message on banner :

Either our Logo + Immigration, Integration, Naturalization

Or our Logo + Incorporation, Domicile, Secretarial Services

And if space allows for it www.alpenmark-example.com as well.

We are looking for a clean design, check our Website for inspiration concerning colors.

```html
<!DOCTYPE html>
<html lang="en">
<head>
<meta charset="utf-8">
<title>Alpenmark Banner Set</title>
<link rel="stylesheet" href="https://fonts.googleapis.com/css2?family=Oswald:wght@500&family=Roboto:wght@700&display=swap">
<style>
:root{
  --red:#ff0000;
  --black:#000000;
  --ink:#231f20;
  --white:#ffffff;
  --panel:rgba(20,20,20,.82);
  --photo-flag:linear-gradient(160deg,#d9d9d9 0%,#9a9a9a 45%,#cfcfcf 100%);
  --photo-awning:linear-gradient(170deg,#5a5a5a 0%,#9b9b9b 35%,#3e3e3e 60%,#8a8a8a 100%);
}
*{margin:0;padding:0;box-sizing:border-box}
html,body{width:1200px;height:862px;overflow:hidden;background:var(--white)}
.stage{position:absolute;left:0;top:0;width:1046px;height:751px;transform:scale(1.1472);transform-origin:0 0}
.box{position:absolute}
.red{background:var(--red)}
.dark{background:var(--black)}
.logo{background:var(--white);display:flex;align-items:center;justify-content:center;gap:5px;border:1px solid #bbb}
.logo-name{font-family:"Oswald",sans-serif;font-weight:500;color:var(--ink);letter-spacing:.02em}
.logo-mark{background:var(--ink);display:inline-block}
.photo-flag{background:var(--photo-flag)}
.photo-awning{background:var(--photo-awning)}
.panel{background:var(--panel);display:flex;flex-direction:column;justify-content:space-around;padding:6px 0 6px 14px}
.services{display:flex;align-items:center}
.service{font-family:"Oswald",sans-serif;font-weight:500;color:var(--white);font-size:15px;display:flex;align-items:center;gap:10px;white-space:nowrap}
.service::before{content:"";width:15px;height:15px;background:var(--red);display:block;flex:none}
.url{font-family:"Roboto",Arial,sans-serif;font-weight:700;color:var(--white);font-size:9.5px;text-align:center;white-space:nowrap;letter-spacing:-.01em}
.url-tight{font-size:9px}
.cta{background:var(--black);display:flex;align-items:center;font-family:"Roboto",Arial,sans-serif;font-weight:700;color:var(--white);font-size:11.5px;gap:8px}
.cta::before{content:"";width:32px;height:100%;background:var(--red);border:2px solid var(--black);flex:none}
.cta-red{display:flex;flex-direction:column;align-items:center;justify-content:center;gap:14px}
.hero{display:flex;align-items:center;justify-content:center;gap:18px}
.hero-name{font-family:"Oswald",sans-serif;font-weight:500;color:var(--ink);font-size:64px;letter-spacing:.03em;white-space:nowrap}
.hero-mark{width:52px;height:52px;background:var(--ink);flex:none}
</style>
</head>
<body>
<div class="stage">

  <!-- Ribbon 990x45 -->
  <div class="box red" style="left:36px;top:44px;width:6px;height:45px"></div>
  <div class="box logo" style="left:42px;top:44px;width:95px;height:45px"><span class="logo-mark" style="width:9px;height:9px"></span><span class="logo-name" style="font-size:14px">ALPENMARK</span></div>
  <div class="box photo-flag" style="left:137px;top:44px;width:64px;height:45px" role="img" aria-label="Swiss flag waving on a flagpole"></div>
  <div class="box dark services" style="left:201px;top:44px;width:528px;height:45px;justify-content:space-around;padding:0 10px">
    <span class="service" style="font-size:18px">IMMIGRATION</span>
    <span class="service" style="font-size:18px">INTEGRATION</span>
    <span class="service" style="font-size:18px">NATURALIZATION</span>
  </div>
  <div class="box red" style="left:729px;top:44px;width:297px;height:45px"></div>
  <div class="box url" style="left:731px;top:62px;width:159px">www.alpenmark-example.com</div>
  <div class="box cta" style="left:892px;top:52px;width:128px;height:31px">KNOW MORE</div>

  <!-- Wide Skyscraper 160x600 -->
  <div class="box red" style="left:40px;top:108px;width:160px;height:6px"></div>
  <div class="box logo" style="left:40px;top:114px;width:160px;height:118px;flex-direction:column"><span class="logo-mark" style="width:18px;height:18px"></span><span class="logo-name" style="font-size:24px">ALPENMARK</span></div>
  <div class="box photo-flag" style="left:40px;top:232px;width:160px;height:138px" role="img" aria-label="Swiss flag waving on a flagpole"></div>
  <div class="box photo-awning" style="left:40px;top:370px;width:160px;height:253px" role="img" aria-label="Striped awnings on a building facade"></div>
  <div class="box panel" style="left:40px;top:478px;width:155px;height:122px;padding-left:21px">
    <span class="service">IMMIGRATION</span>
    <span class="service">INTEGRATION</span>
    <span class="service">NATURALIZATION</span>
  </div>
  <div class="box red cta-red" style="left:40px;top:625px;width:160px;height:83px">
    <span class="url">www.alpenmark-example.com</span>
    <span class="cta" style="width:128px;height:32px">KNOW MORE</span>
  </div>

  <!-- Medium Rectangle 300x250 -->
  <div class="box red" style="left:231px;top:107px;width:300px;height:86px"></div>
  <div class="box logo" style="left:231px;top:112px;width:141px;height:81px;flex-direction:column;border:none"><span class="logo-mark" style="width:14px;height:14px"></span><span class="logo-name" style="font-size:21px">ALPENMARK</span></div>
  <div class="box url" style="left:374px;top:121px;width:155px">www.alpenmark-example.com</div>
  <div class="box cta" style="left:389px;top:146px;width:128px;height:33px">KNOW MORE</div>
  <div class="box photo-awning" style="left:231px;top:193px;width:300px;height:164px" role="img" aria-label="Striped awnings on a building facade"></div>
  <div class="box photo-flag" style="left:240px;top:217px;width:138px;height:123px" role="img" aria-label="Swiss flag waving on a flagpole"></div>
  <div class="box panel" style="left:378px;top:217px;width:148px;height:123px">
    <span class="service">IMMIGRATION</span>
    <span class="service">INTEGRATION</span>
    <span class="service">NATURALIZATION</span>
  </div>

  <!-- Brand name -->
  <div class="box hero" style="left:568px;top:325px;width:425px">
    <span class="hero-mark"></span><span class="hero-name">ALPENMARK</span>
  </div>

  <!-- Leaderboard 728x90 -->
  <div class="box red" style="left:231px;top:618px;width:6px;height:90px"></div>
  <div class="box logo" style="left:237px;top:618px;width:143px;height:90px;flex-direction:column"><span class="logo-mark" style="width:12px;height:12px"></span><span class="logo-name" style="font-size:21px">ALPENMARK</span></div>
  <div class="box photo-flag" style="left:380px;top:618px;width:135px;height:90px" role="img" aria-label="Swiss flag waving on a flagpole"></div>
  <div class="box photo-awning" style="left:515px;top:618px;width:293px;height:90px" role="img" aria-label="Striped awnings on a building facade"></div>
  <div class="box panel" style="left:595px;top:622px;width:160px;height:84px;padding:2px 0 2px 18px">
    <span class="service">IMMIGRATION</span>
    <span class="service">INTEGRATION</span>
    <span class="service">NATURALIZATION</span>
  </div>
  <div class="box red cta-red" style="left:808px;top:618px;width:151px;height:90px;gap:16px">
    <span class="url url-tight">www.alpenmark-example.com</span>
    <span class="cta" style="width:127px;height:32px">KNOW MORE</span>
  </div>

</div>
</body>
</html>
```